Upbeat Accouting Package Flyer

I am looking for a 1 page (front, or front and back) flyer that will become our marketing for our accounting services. We are looking for something a little different and we are catering to the small retail shop owners. We have 3 accounting packages we would like to display and then some add-ons. I have included our logo that must be included in the design. I have uploaded the accounting package information as well.
Target Market(s)
Small Retail Shop Owners
Industry/Entity Type
Accounting
Colors
Designer to choose colors to be used in the design.
Requirements
Must have
- A casual feel. We are not your typical accountants who are very professional and "stuffy". I want it to feel like we are all family.
Nice to have
- I would like to incorporate some sort of retail theme.
- We have a couple of taglines we like to use and it would be great if they could be included. They are "We know you CAN do the accounting, but do you WANT to?" and "We allow you to get back to what's important."
Should not have
- Typical stock accounting photos of people shaking hands, large office buildings, etc.

```html
<!DOCTYPE html>
<html lang="en">
<head>
<meta charset="utf-8">
<title>Brightline Accounting Packages Flyer</title>
<link href="https://fonts.googleapis.com/css2?family=Montserrat:wght@300;400;600;800&family=Open+Sans:wght@400;600&family=Roboto+Condensed:wght@400&display=swap" rel="stylesheet">
<style>
  :root{
    --cyan:#0bb8d6;
    --cyan-light:#6fdcef;
    --ink:#2b2b2b;
    --grey:#4a4a4a;
    --paper:#ffffff;
    --paper-soft:#f3f4f5;
    --stage:#e4e6e8;
  }
  *{margin:0;padding:0;box-sizing:border-box}
  html,body{width:1200px;height:1200px;overflow:hidden;background:var(--stage)}
  .flyer{position:absolute;left:190px;top:20px;width:820px;height:1160px;background:var(--paper);overflow:hidden;box-shadow:0 4px 18px rgba(0,0,0,.18);font-family:"Open Sans",sans-serif;color:var(--ink)}
  .backdrop{position:absolute;inset:0}
  .brand{position:absolute;left:40px;top:48px;font-family:"Montserrat",sans-serif;font-weight:600;font-size:52px;letter-spacing:-1px;color:var(--ink)}
  .headline{position:absolute;left:412px;top:78px;font-family:"Montserrat",sans-serif;font-weight:300;font-size:29px;line-height:40px;color:#fff;text-transform:uppercase}
  .headline b{font-weight:800}
  .headline .dark{color:var(--ink)}
  .headline .big{font-size:36px;line-height:42px}
  .about{position:absolute;left:462px;top:400px;width:325px;text-align:center}
  .about h2{font-family:"Montserrat",sans-serif;font-weight:800;font-size:23px;color:var(--cyan);margin-bottom:14px}
  .about p{font-size:13.6px;line-height:18.5px;font-weight:600;color:var(--ink)}
  .packages-banner{position:absolute;left:263px;top:580px;width:464px;height:54px}
  .packages-banner span{position:absolute;left:0;right:55px;top:0;line-height:54px;text-align:center;font-family:"Montserrat",sans-serif;font-weight:800;font-size:23px;color:#fff}
  .column{position:absolute;top:682px}
  .column h3{display:flex;align-items:center;gap:14px;font-family:"Montserrat",sans-serif;font-weight:600;font-size:18px;color:var(--grey);margin-bottom:12px}
  .hex-icon{width:44px;height:48px;flex:none}
  .column ul{list-style:none;font-family:"Roboto Condensed",sans-serif;font-size:10px;line-height:13px;color:var(--ink)}
  .column li{position:relative;padding-left:15px;margin-bottom:6px}
  .column li::before{content:"";position:absolute;left:2px;top:3px;width:6px;height:6px;background:var(--cyan);transform:rotate(45deg);box-shadow:0 0 0 1.5px #1b5a66 inset}
  .develop{left:40px;width:200px}
  .grow{left:274px;width:300px}
  .grow .split{display:flex;gap:6px}
  .grow ul{width:152px}
  .relax{left:604px;width:185px}
  .divider{position:absolute;top:690px;width:1px;height:210px;background:#b8b8b8}
  .extra{position:absolute;left:40px}
  .extra h4{display:flex;align-items:center;gap:14px;font-family:"Montserrat",sans-serif;font-weight:800;font-size:17px;color:var(--ink)}
  .extra h4 em{font-style:normal;color:var(--cyan)}
  .round-icon{width:26px;height:26px;flex:none}
  .extra p{font-size:14px;line-height:18.5px;color:var(--ink);margin-top:12px;padding-left:7px}
  .portal{top:926px;width:640px}
  .options{top:1020px}
  .contact{position:absolute;right:36px;top:1050px;text-align:right;color:#fff;font-size:12.8px;font-weight:600}
  .contact li{list-style:none;display:flex;align-items:center;justify-content:flex-end;gap:10px;height:31px}
  .contact svg{width:20px;height:20px}
</style>
</head>
<body>
<main class="flyer">
  <svg class="backdrop" viewBox="0 0 820 1160" aria-hidden="true">
    <defs>
      <linearGradient id="photoTone" x1="0" y1="0" x2="1" y2="1">
        <stop offset="0" stop-color="#d9d4cf"/>
        <stop offset=".5" stop-color="#8e8f93"/>
        <stop offset="1" stop-color="#3c3d42"/>
      </linearGradient>
    </defs>
    <path d="M0 0 H380 V300 L0 320 Z" fill="var(--paper-soft)"/>
    <path d="M345 0 H820 V294 L440 394 L268 640 L0 640 L0 305 L300 172 Q385 125 345 0 Z" fill="var(--cyan-light)"/>
    <path d="M362 0 H820 V286 L433 387 L262 630 L0 628 L0 318 L305 186 Q398 136 362 0 Z" fill="var(--cyan)"/>
    <path d="M820 160 L700 225 Q665 248 712 252 L820 268 Z" fill="var(--cyan-light)"/>
    <path d="M338 1160 L820 962 V1160 Z" fill="var(--cyan)"/>
    <path d="M240 196 L438 306 V530 L240 640 L42 530 V306 Z" fill="#fff" stroke="#fff" stroke-width="8" stroke-linejoin="round"/>
    <path d="M240 206 L428 311 V525 L240 630 L52 525 V311 Z" fill="url(#photoTone)" role="img" aria-label="Photo: small shop owners working together at a laptop with connected retail icons"/>
  </svg>

  <div class="brand">brightline</div>

  <h1 class="headline">
    We know you can<br>
    do the <b class="dark">accounting</b><br>
    <span class="big"><span class="dark">but</span> <b>do you</b></span><br>
    <span class="big"><b>want to?</b></span>
  </h1>

  <section class="about">
    <h2>ABOUT US</h2>
    <p>Brightline Tax and Accounting Inc. is located in Fairview, KS and is an expert in all areas of accounting, bookkeeping, consulting, outsourcing, payroll and business services.</p>
  </section>

  <div class="packages-banner">
    <svg viewBox="0 0 464 54" width="464" height="54" aria-hidden="true"><path d="M0 0 H440 L420 27 L464 54 H0 L24 27 Z" fill="var(--ink)"/></svg>
    <span>ACCOUNTING PACKAGES</span>
  </div>

  <section class="column develop">
    <h3><svg class="hex-icon" viewBox="0 0 44 48" aria-hidden="true"><path d="M22 1 L43 13 V35 L22 47 L1 35 V13 Z" fill="var(--cyan)"/><path d="M12 33 L19 24 L24 29 L32 17 M27 17 H32 V22" stroke="#fff" stroke-width="2.4" fill="none" stroke-linecap="round" stroke-linejoin="round"/></svg>DEVELOP</h3>
    <ul>
      <li>$300/mo when paid annually $325/mo billed monthly</li>
      <li>LedgerCloud Online subscription</li>
      <li>Free accounting setup</li>
      <li>Weekly transaction processing</li>
      <li>Monthly account reconciliation (up to 2 accounts)</li>
      <li>Monthly financial statements by the 15th of the month</li>
    </ul>
  </section>

  <div class="divider" style="left:254px"></div>

  <section class="column grow">
    <h3><svg class="hex-icon" viewBox="0 0 44 48" aria-hidden="true"><path d="M22 1 L43 13 V35 L22 47 L1 35 V13 Z" fill="var(--cyan)"/><path d="M11 31 Q22 37 33 29 M22 30 V18 M22 22 Q15 20 15 14 Q21 14 22 20 M22 20 Q24 13 30 13 Q30 19 22 21" stroke="#fff" stroke-width="2.2" fill="none" stroke-linecap="round"/></svg>GROW</h3>
    <div class="split">
      <ul>
        <li>$550/mo billed annually; $575/mo billed monthly</li>
        <li>LedgerCloud Online subscription</li>
        <li>Free accounting setup</li>
        <li>Weekly transaction processing</li>
        <li>Monthly account reconciliation (up to 4 accounts)</li>
        <li>1 Custom Report</li>
      </ul>
      <ul>
        <li>Monthly financial statements by the 10th of the month</li>
        <li>Client portal access for document sharing</li>
        <li>Accounts Payable</li>
        <li>Monthly Scorecard (customized metric tracking for your business)</li>
      </ul>
    </div>
  </section>

  <div class="divider" style="left:581px"></div>

  <section class="column relax">
    <h3><svg class="hex-icon" viewBox="0 0 44 48" aria-hidden="true"><path d="M22 1 L43 13 V35 L22 47 L1 35 V13 Z" fill="var(--cyan)"/><path d="M12 22 L20 31 L33 16" stroke="#fff" stroke-width="3" fill="none" stroke-linecap="round" stroke-linejoin="round"/></svg>RELAX</h3>
    <ul>
      <li>$850/mo billed annually; $875/mo billed monthly</li>
      <li>LedgerCloud Online subscription</li>
      <li>Free accounting setup</li>
      <li>Weekly transaction processing</li>
      <li>Monthly account reconciliation (up to 5-10 accounts)</li>
      <li>Monthly financial statements by the 5th of the month</li>
    </ul>
  </section>

  <section class="extra portal">
    <h4><svg class="round-icon" viewBox="0 0 26 26" aria-hidden="true"><circle cx="13" cy="13" r="13" fill="var(--ink)"/><circle cx="10" cy="10" r="3" fill="#fff"/><path d="M5 19 Q10 12 15 19 Z" fill="#fff"/><rect x="15" y="9" width="6" height="9" fill="#fff"/></svg><span><em>CLIENT PORTAL ACCESS</em> FOR DOCUMENT SHARING</span></h4>
    <p>2 Custom Reports | Accounts Payable | Invoicing and accounts receivable | Weekly Scorecard (customized metric tracking for your business)</p>
  </section>

  <section class="extra options">
    <h4><svg class="round-icon" viewBox="0 0 26 26" aria-hidden="true"><circle cx="13" cy="13" r="13" fill="var(--ink)"/><path d="M13 7 V19 M7 13 H19" stroke="#fff" stroke-width="2.4"/></svg><span><em>ADDITIONAL</em> OPTIONS</span></h4>
    <p>Payroll – 1-10 employees $85/mo; 11-30 employees $175/mo<br>Sales tax - $30/mo per state | Corporate taxes $50/mo<br>Owner taxes - $25/mo</p>
  </section>

  <ul class="contact">
    <li>(555) 214-0387 <svg viewBox="0 0 20 20" aria-hidden="true"><path d="M5 2 L8 6 L6 8 Q8 12 12 14 L14 12 L18 15 L16 18 Q6 17 2 5 Z" fill="var(--ink)"/></svg></li>
    <li>hello@brightline-books.com <svg viewBox="0 0 20 20" aria-hidden="true"><rect x="1" y="5" width="18" height="12" fill="var(--ink)"/><path d="M1 5 L10 12 L19 5" stroke="#fff" stroke-width="1.4" fill="none"/></svg></li>
    <li>4410 W. Elm Street Fairview, KS 66000 <svg viewBox="0 0 20 20" aria-hidden="true"><path d="M10 1 Q16 1 16 7 Q16 11 10 17 Q4 11 4 7 Q4 1 10 1 Z" fill="none" stroke="var(--ink)" stroke-width="2"/><circle cx="10" cy="7" r="2" fill="var(--ink)"/><path d="M5 18 H15" stroke="var(--ink)" stroke-width="1.6"/></svg></li>
  </ul>
</main>
</body>
</html>
```